Brisko - Instant events application for super cool and busy people

I need web design (NOT HTML/CSS just design) for a mobile (responsive) application called Brisko. Additionally, I need a logo with the tag line "Where we headin' now!"

The style should be cartoony retro style, here is a mood board to get the idea of the style that I am looking for:

https://www.pinvaultly.net/dkemlerto/brisko/

Concept:

Instant meetup to tell your friends, a select group of friends or everyone that you would like to do something i.e. go for a drink, have a meal, go rock climbing… anything. The premise is that it’s not pre planning an event its something that you want to happen now, or within a few hours max.

After creating the event people within a specific distance that you have invited will be notified so they can come along if they wish.

Pages/Sections:

Home Page:
- Login with yoohalo
- Description of service, just add lorum ipsum for now but I will want a cartoon slideshow thing explaining the process potentially later.

Start an event
- Say what you want to do. Title + Description
- Say where you want to do it (either a specific place, or a general area). -- -- Also specify a distance of the people within that range to be notified.
- Select individual yoohalo friends, or a premade group of friends or anyone
- Specify an indication of time i.e. ‘now’, ‘in xxx’
- Upload an event image (optional)

Show Notifications
- Some kind of notification/messaging feed indicator to show that you have received a new notification/message
- List of notifications/message
- Event notification will show ‘xxx vants to do yyy’ with link to event page

Event Page
- Details of event
- Distance from you currently (i.e. ‘xxx is 1 mile away’)
- Show who’s accepted/rejected event
- Ability to confirm that you are coming or not
- Ability to add messages to the event
- Generic messages and the ability to suggest specific/alternative venues
- Upload images

All this will appear in the users notifications feed if they are attending the event.

Target Market(s)

20/30 something's who have large social circles and find it difficult to commit to events too far in the future.

Industry/Entity Type

Events

Number of Pages Required

5+ page

Font styles to use
Decorative
Script

Requirements
Must have
• Just need the PSD's or similar to slice the image. Also, any fonts used.

```html
<!DOCTYPE html>
<html lang="en">
<head>
<meta charset="utf-8">
<title>Brisko — Where we headin' now!</title>
<link rel="stylesheet" href="https://fonts.googleapis.com/css2?family=Arimo:wght@400;700&family=Lora:ital,wght@1,700&display=swap">
<style>
  :root {
    --paper: #e6bd85;
    --paper-light: #f4d8a8;
    --paper-edge: #d9a86c;
    --brand-red: #c8401f;
    --text-red: #c0252a;
    --figure-tone: #d98f6a;
    --figure-deep: #b9553f;
    --button-top: #4f6fae;
    --button-bottom: #2f4c8a;
    --button-divider: #22396b;
    --button-text: #ffffff;
    --footer: #3a2420;
    --footer-rule: #5b3b31;
    --footer-text: #f1e6dc;
  }
  * { box-sizing: border-box; margin: 0; padding: 0; }
  html, body {
    width: 1200px;
    height: 2461px;
    overflow: hidden;
  }
  body {
    font-family: "Arimo", Arial, sans-serif;
    background: var(--paper);
  }
  .app-screen {
    width: 1200px;
    height: 2461px;
    display: flex;
    flex-direction: column;
  }
  .home {
    flex: 1;
    display: flex;
    flex-direction: column;
    align-items: center;
    padding: 150px 120px 0;
    background:
      radial-gradient(ellipse 900px 700px at 50% 8%, var(--paper-light) 0%, rgba(244,216,168,0) 75%),
      linear-gradient(180deg, var(--paper) 0%, var(--paper-edge) 100%);
  }
  .brand {
    display: flex;
    flex-direction: column;
    align-items: center;
  }
  .brand-mark {
    width: 130px;
    height: 130px;
    border-radius: 50%;
    background: var(--brand-red);
    margin-bottom: 30px;
  }
  .brand-name {
    font-family: "Arimo", Arial, sans-serif;
    font-weight: 700;
    font-size: 230px;
    line-height: 1;
    color: var(--brand-red);
    letter-spacing: -4px;
  }
  .tagline {
    font-family: "Lora", Georgia, serif;
    font-style: italic;
    font-weight: 700;
    font-size: 60px;
    color: var(--text-red);
    margin-top: 30px;
  }
  .hero-figure {
    width: 520px;
    height: 640px;
    margin-top: 110px;
    border-radius: 260px 260px 40px 40px;
    background: radial-gradient(ellipse at 50% 35%, var(--figure-tone) 0%, var(--figure-deep) 70%, rgba(185,85,63,0.25) 100%);
    opacity: 0.85;
  }
  .intro {
    margin-top: 120px;
    font-size: 49px;
    line-height: 1.36;
    color: var(--text-red);
    text-align: center;
    max-width: 980px;
  }
  .login-button {
    margin-top: 80px;
    width: 870px;
    height: 140px;
    display: flex;
    align-items: stretch;
    border-radius: 18px;
    overflow: hidden;
    background: linear-gradient(180deg, var(--button-top) 0%, var(--button-bottom) 100%);
    box-shadow: 0 4px 10px rgba(0,0,0,0.25);
    color: var(--button-text);
    text-decoration: none;
  }
  .login-button__icon {
    width: 150px;
    display: flex;
    align-items: center;
    justify-content: center;
    border-right: 3px solid var(--button-divider);
  }
  .login-button__icon span {
    width: 60px;
    height: 60px;
    background: var(--button-text);
    border-radius: 6px;
    opacity: 0.9;
  }
  .login-button__label {
    flex: 1;
    display: flex;
    align-items: center;
    justify-content: center;
    gap: 16px;
    font-size: 56px;
  }
  .login-button__label strong { font-weight: 700; }
  .site-footer {
    height: 180px;
    background: var(--footer);
    border-top: 8px solid var(--footer-rule);
    display: flex;
    align-items: center;
    justify-content: center;
    color: var(--footer-text);
    font-size: 40px;
  }
</style>
</head>
<body>
  <div class="app-screen">
    <main class="home">
      <header class="brand">
        <span class="brand-mark" aria-hidden="true"></span>
        <h1 class="brand-name">Brisko</h1>
        <p class="tagline">Where we headin' now!</p>
      </header>

      <div class="hero-figure" role="img" aria-label="Retro cartoon illustration of a woman in a polka-dot blouse pointing with her thumb"></div>

      <p class="intro">Lorem ipsum dolor sit amet, consectetuer adipiscing elit, sed diam nonummy nibh euismod tincidunt ut laoreet dolore magna aliquam erat volutpat.</p>

      <a class="login-button" href="#">
        <span class="login-button__icon" aria-hidden="true"><span></span></span>
        <span class="login-button__label">Login with <strong>yoohalo</strong></span>
      </a>
    </main>

    <footer class="site-footer">© 2015.&nbsp; Brisko. All rights reserved.</footer>
  </div>
</body>
</html>
```